Business Card for a Dental Office

The design should communicate integrity, quality and reliability. We also want the card look elegant, simple, but still stand out, different from the traditional-dental-office business card.

Industry/Entity Type

Business

```html
<!DOCTYPE html>
<html lang="en">
<head>
<meta charset="utf-8">
<title>Harlow Dental Studio – Business Card</title>
<link href="https://fonts.googleapis.com/css2?family=Bebas+Neue&family=Source+Sans+3:wght@400;600&display=swap" rel="stylesheet">
<style>
  :root {
    --backdrop: #e4e4e4;
    --card-black: #000000;
    --ink-white: #ffffff;
    --brand-yellow: #f2e51c;
    --tagline-gold: #d9b82c;
    --back-top: #f3ec17;
    --back-bottom: #c9ae2c;
    --ink-dark: #111111;
  }
  * { margin: 0; padding: 0; box-sizing: border-box; }
  html, body {
    width: 1200px; height: 900px; overflow: hidden;
    background: var(--backdrop);
  }
  .canvas { position: relative; width: 1200px; height: 900px; }

  .card {
    position: absolute; top: 306px;
    width: 440px; height: 271px;
    border-radius: 12px;
    box-shadow: 0 2px 6px rgba(0,0,0,0.18);
  }
  .card--front { left: 149px; background: var(--card-black); }
  .card--back {
    left: 608px;
    background: linear-gradient(180deg, var(--back-top) 0%, var(--back-bottom) 100%);
  }

  .brand { position: absolute; left: 56px; top: 34px; display: flex; align-items: center; gap: 12px; }
  .brand__square { width: 30px; height: 30px; background: var(--brand-yellow); }
  .brand__text { display: flex; flex-direction: column; }
  .brand__name {
    font-family: "Bebas Neue", sans-serif;
    font-size: 32px; line-height: 30px; letter-spacing: 0.3px;
    color: var(--ink-white);
  }
  .brand__tagline {
    font-family: "Bebas Neue", sans-serif;
    font-size: 14.5px; line-height: 14px; letter-spacing: 0.8px;
    color: var(--tagline-gold);
  }

  .person {
    position: absolute; right: 235px; top: 144px;
    text-align: right;
    font-family: "Source Sans 3", sans-serif;
    color: var(--ink-white);
  }
  .person__name { font-size: 18px; font-weight: 600; color: var(--brand-yellow); line-height: 20px; }
  .person__role { font-size: 13px; line-height: 18px; }
  .person__address { margin-top: 10px; font-size: 13px; line-height: 16px; }

  .contacts {
    position: absolute; left: 232px; top: 143px;
    list-style: none;
    font-family: "Source Sans 3", sans-serif;
    font-size: 13px; line-height: 16px;
    color: var(--ink-white);
  }
  .contacts li { display: flex; align-items: center; gap: 9px; }
  .contacts svg { width: 9px; height: 9px; fill: var(--brand-yellow); flex: none; }

  .back-brand {
    position: absolute; inset: 0;
    display: flex; align-items: center; justify-content: center; gap: 12px;
  }
  .back-brand__square { width: 40px; height: 40px; background: var(--ink-dark); }
  .back-brand__name {
    font-family: "Bebas Neue", sans-serif;
    font-size: 40px; letter-spacing: 0.5px;
    color: var(--ink-dark);
  }
</style>
</head>
<body>
<main class="canvas">
  <section class="card card--front" aria-label="Business card front">
    <div class="brand">
      <span class="brand__square" aria-hidden="true"></span>
      <div class="brand__text">
        <span class="brand__name">Harlow Dental Studio</span>
        <span class="brand__tagline">Your smile is your gift to others</span>
      </div>
    </div>

    <div class="person">
      <p class="person__name">Daniel Mercer</p>
      <p class="person__role">Managing Director</p>
      <p class="person__address">1234, Address Goes Here<br>Country Name, 123456</p>
    </div>

    <ul class="contacts">
      <li><svg viewBox="0 0 10 10" aria-hidden="true"><path d="M3 0h4a1 1 0 0 1 1 1v8a1 1 0 0 1-1 1H3a1 1 0 0 1-1-1V1a1 1 0 0 1 1-1zm0 1.5v6h4v-6z"/></svg>123-456-7890</li>
      <li><svg viewBox="0 0 10 10" aria-hidden="true"><path d="M0 3c2-2 8-2 10 0l-1 1.5-2-.5V3H3v1L1 4.5zM2 5h6l1 4H1z"/></svg>123-456-7890</li>
      <li><svg viewBox="0 0 10 10" aria-hidden="true"><path d="M3 0h5v3H3zM1 3h8a1 1 0 0 1 1 1v6H0V4a1 1 0 0 1 1-1zm2 3v2h4V6z"/></svg>123-456-7890</li>
      <li><svg viewBox="0 0 10 10" aria-hidden="true"><path d="M0 2h10v1L5 6 0 3zm0 2.2L5 7l5-2.8V8H0z"/></svg>info@youremail.com</li>
      <li><svg viewBox="0 0 10 10" aria-hidden="true"><path d="M7 0l3 3-6 6H1V6zM2 7v1h1z"/></svg>www.yourweb.com</li>
    </ul>
  </section>

  <section class="card card--back" aria-label="Business card back">
    <div class="back-brand">
      <span class="back-brand__square" aria-hidden="true"></span>
      <span class="back-brand__name">Harlow Dental Studio</span>
    </div>
  </section>
</main>
</body>
</html>
```